RW Frameworks Inc Business cards

We need business cards using our existing logo but slightly modified. Right now the logo says RW Framework Masonry. We want to keep the RW part of the design, but replace the Framework Masonry portion with "FRAMEWORKS". Please see the attached file.
Ideally this would be a blank template so we can add Different Names, titles, and phone numbers later.
On the one side we want only the logo and on the other side the detail. I'm attaching an example for you to see.
Please reach out with any other questions. Our address and other details will be given out once we find a design we like.

Target Market(s)

Construction Industry

```html
<!DOCTYPE html>
<html lang="en">
<head>
<meta charset="utf-8">
<title>RW Frameworks Business Cards</title>
<link rel="stylesheet" href="https://fonts.googleapis.com/css2?family=Roboto:wght@400;500&display=swap">
<style>
  :root {
    --brand-blue: #1e76be;
    --ink-grey: #555a60;
    --text-dark: #2b2e33;
    --card-white: #ffffff;
    --backdrop: #e7e8ea;
  }
  * { box-sizing: border-box; margin: 0; padding: 0; }
  html, body { width: 1200px; height: 913px; overflow: hidden; }
  body {
    background: var(--backdrop);
    font-family: "Roboto", Arial, sans-serif;
    position: relative;
  }
  .card {
    position: absolute;
    left: 250px;
    width: 700px;
    height: 400px;
    box-shadow: 0 6px 18px rgba(0,0,0,0.18);
  }
  .card--front { top: 36px; background: var(--brand-blue); }
  .card--back { top: 477px; background: var(--card-white); }

  .wordmark {
    display: flex;
    align-items: center;
    gap: 16px;
    font-weight: 500;
    letter-spacing: 2px;
    white-space: nowrap;
  }
  .wordmark__square { width: 22px; height: 22px; flex: none; }
  .card--front .wordmark {
    position: absolute;
    left: 50%; top: 50%;
    transform: translate(-50%, -50%);
    color: var(--card-white);
    font-size: 46px;
  }
  .card--front .wordmark__square { background: var(--card-white); }

  .logo-area {
    position: absolute;
    left: 0; top: 0;
    width: 374px; height: 400px;
    padding: 40px 32px 0;
    display: flex;
    align-items: center;
    justify-content: center;
  }
  .card--back .wordmark {
    color: var(--brand-blue);
    font-size: 28px;
    letter-spacing: 1px;
    gap: 12px;
  }
  .card--back .wordmark__square { background: var(--brand-blue); width: 16px; height: 16px; }

  .divider {
    position: absolute;
    left: 374px; top: 70px;
    width: 2px; height: 260px;
    background: var(--brand-blue);
  }
  .details { position: absolute; left: 404px; top: 74px; right: 24px; }
  .details__name {
    color: var(--brand-blue);
    font-size: 24px;
    font-weight: 500;
    letter-spacing: 0.5px;
    white-space: nowrap;
  }
  .details__title {
    color: var(--ink-grey);
    font-size: 14px;
    letter-spacing: 1px;
    margin-top: 4px;
  }
  .details__address {
    color: var(--text-dark);
    font-size: 13px;
    line-height: 1.45;
    margin-top: 22px;
  }
  .contact-list { list-style: none; margin-top: 20px; }
  .contact-list li {
    display: flex; align-items: center; gap: 10px;
    color: var(--text-dark);
    font-size: 15px;
    line-height: 1.8;
    white-space: nowrap;
  }
  .contact-list svg { width: 15px; height: 15px; fill: var(--brand-blue); flex: none; }
</style>
</head>
<body>
  <section class="card card--front" aria-label="Card front">
    <div class="wordmark"><span class="wordmark__square"></span>RW FRAMEWORKS</div>
  </section>

  <section class="card card--back" aria-label="Card back">
    <div class="logo-area">
      <div class="wordmark"><span class="wordmark__square"></span>RW FRAMEWORKS</div>
    </div>
    <div class="divider"></div>
    <div class="details">
      <p class="details__name">DANIEL OKAFOR</p>
      <p class="details__title">DIRECTOR</p>
      <p class="details__address">48 Harbour Lane, Eastfield,<br>Northgate (Eastfield Station Exit B)</p>
      <ul class="contact-list">
        <li>
          <svg viewBox="0 0 24 24" aria-hidden="true"><path d="M6.6 10.8a15.1 15.1 0 0 0 6.6 6.6l2.2-2.2a1 1 0 0 1 1-.25 11.4 11.4 0 0 0 3.6.57 1 1 0 0 1 1 1V20a1 1 0 0 1-1 1A17 17 0 0 1 3 4a1 1 0 0 1 1-1h3.5a1 1 0 0 1 1 1c0 1.25.2 2.45.57 3.57a1 1 0 0 1-.25 1z"/></svg>
          5550123456
        </li>
        <li>
          <svg viewBox="0 0 24 24" aria-hidden="true"><path d="M2 5h20v14H2z"/><path d="M3 6.5l9 6.5 9-6.5" fill="none" stroke="#fff" stroke-width="1.6"/></svg>
          info@rwframeworks.com
        </li>
        <li>
          <svg viewBox="0 0 24 24" aria-hidden="true"><circle cx="12" cy="12" r="10"/><path d="M2 12h20M12 2c3 3 3 17 0 20M12 2c-3 3-3 17 0 20" fill="none" stroke="#fff" stroke-width="1.3"/></svg>
          www.rwframeworks.com
        </li>
      </ul>
    </div>
  </section>
</body>
</html>
```